Design and Renovation Company Luxury Business Card

I want to create a luxury business card for a Design and Renovation Firm . We will use our current logo. The company name is 742KAVO. We do not want anything standard. We need a very unique concept.
Please see uploaded inspiration. I really like the textured paper option. I would like the card to be thick with debossing, and/or embossing options. The logo has orange in it but I would like to see the card with and without the orange. I think the orange may make the company feel less high-end. The goal is to elevate the logo not match its vibe per se of the logo. We want something very unique, not standard at all!
I would like a space for :
Logo,
Name,
Position,
Email,
Office number,
Website Address,
Business Address,
Thank you!
Have fun!
Target Market(s)
Home owners Age 35 +
Industry/Entity Type
Design and Renovation
Contact Information for Business Card
Logo, Name, Position, Email, Office number, Website Address, Business Address,.
Colors
Designer to choose colors to be used in the design.
Requirements
Must have
- A luxury designer feel. Must be black or dark grey but open to other luxury ideas.
Nice to have
- Gold, silver, black embossing or debossing. Textured paper design.
Should not have
- A cheap look and feel.

```html
<!DOCTYPE html>
<html lang="en">
<head>
<meta charset="UTF-8">
<title>742KAVO Business Card</title>
<link href="https://fonts.googleapis.com/css2?family=Montserrat:wght@400;500;600&display=swap" rel="stylesheet">
<style>
  :root {
    --backdrop: #9b9b9b;
    --paper-white: #f6f6f4;
    --paper-black: #1e1e1e;
    --ink: #1f1f1f;
    --ink-soft: #3a3a3a;
    --accent: #f0901c;
    --edge: #d97a0c;
    --silver: #ececec;
  }
  * { box-sizing: border-box; margin: 0; padding: 0; }
  html, body {
    width: 1200px; height: 956px; overflow: hidden;
    background: var(--backdrop);
    font-family: "Montserrat", Arial, sans-serif;
  }
  .canvas { position: relative; width: 1200px; height: 956px; }

  .card {
    position: absolute;
    width: 640px; height: 366px;
    border-radius: 2px;
    border-bottom: 4px solid var(--edge);
    box-shadow: 0 18px 36px rgba(0,0,0,0.28);
  }
  .card--front { left: 150px; top: 80px; background: var(--paper-white); }
  .card--back  { left: 410px; top: 500px; background: var(--paper-black); }

  /* Company name */
  .company-name {
    position: absolute;
    font-weight: 500;
    letter-spacing: 0.04em;
    line-height: 1;
    white-space: nowrap;
  }
  .card--front .company-name { right: 52px; top: 76px; font-size: 46px; color: var(--ink); }
  .card--back .company-name {
    left: 50%; top: 50%; transform: translate(-50%, -50%);
    font-size: 80px; color: var(--silver);
  }

  /* Front details */
  .person { position: absolute; left: 52px; top: 108px; }
  .person__name { font-size: 22px; font-weight: 600; color: var(--accent); letter-spacing: 0.03em; }
  .person__role { font-size: 12px; color: var(--ink-soft); margin-top: 2px; }

  .divider {
    position: absolute; left: 52px; right: 52px; top: 172px;
    height: 1.5px; background: var(--accent);
  }

  .contacts { position: absolute; left: 52px; top: 192px; list-style: none; }
  .contacts__item {
    display: flex; align-items: center; gap: 10px;
    font-size: 12.5px; color: var(--ink); line-height: 1; margin-bottom: 9px;
  }
  .contacts__icon { width: 12px; height: 12px; fill: none; stroke: var(--accent); stroke-width: 1.6; }

  .address {
    position: absolute; right: 52px; bottom: 36px;
    font-size: 12.5px; font-style: normal; color: var(--ink);
    line-height: 1.45; text-align: left;
  }
</style>
</head>
<body>
<main class="canvas">

  <section class="card card--front" aria-label="Business card front">
    <p class="company-name">742KAVO</p>

    <div class="person">
      <p class="person__name">DANE CORWIN</p>
      <p class="person__role">Medical Director</p>
    </div>

    <div class="divider"></div>

    <ul class="contacts">
      <li class="contacts__item">
        <svg class="contacts__icon" viewBox="0 0 12 12" aria-hidden="true"><path d="M2.5 1.5 L4.5 1.5 L5.2 4 L4 5 Q5 7.2 7 8 L8 6.8 L10.5 7.5 L10.5 9.5 Q6 10.5 2 5.5 Q1.5 3.5 2.5 1.5 Z"/></svg>
        (000)555-0142
      </li>
      <li class="contacts__item">
        <svg class="contacts__icon" viewBox="0 0 12 12" aria-hidden="true"><rect x="1" y="2.5" width="10" height="7"/><path d="M1 2.5 L6 6.5 L11 2.5"/></svg>
        hello@742kavo.com
      </li>
      <li class="contacts__item">
        <svg class="contacts__icon" viewBox="0 0 12 12" aria-hidden="true"><circle cx="6" cy="6" r="4.8"/><path d="M1.2 6 H10.8 M6 1.2 Q3.5 6 6 10.8 M6 1.2 Q8.5 6 6 10.8"/></svg>
        www.742kavo.com
      </li>
    </ul>

    <address class="address">
      418 Harbor Crest Road Suite<br>
      12 Brookfield, New York 10520
    </address>
  </section>

  <section class="card card--back" aria-label="Business card back">
    <p class="company-name">742KAVO</p>
  </section>

</main>
</body>
</html>
```